Hiring Infographic

We need an infographic for displaying on a website and sharing via social media. Attached is an example of a prior infographic developed for the client for reference (Orchard Ledger). The data for the new infographic is in the attached Mocrosoft Word document about hiring.

Media

```html
<!DOCTYPE html>
<html lang="en">
<head>
<meta charset="utf-8">
<title>Hiring the Right People</title>
<link href="https://fonts.googleapis.com/css2?family=Bebas+Neue&family=Oswald:wght@500;600&family=Jost:ital,wght@0,400;0,600;1,400&family=Lobster+Two:ital,wght@1,700&display=swap" rel="stylesheet">
<style>
  :root{
    --paper:#f3f0e5;
    --ink:#2b2b3b;
    --navy:#24263a;
    --red:#dd5b5b;
    --rose:#c9505a;
    --blush:#eda7a7;
    --teal:#7dcfd9;
    --teal-deep:#4fb0bc;
    --orange:#f4a93c;
    --yellow:#f7e27a;
    --globe:#3a9aa6;
  }
  *{box-sizing:border-box;margin:0;padding:0}
  html,body{width:1200px;height:3564px;overflow:hidden;background:var(--paper)}
  body{position:relative;font-family:"Jost","Century Gothic",sans-serif;color:var(--ink)}
  .abs{position:absolute}
  .title{left:0;width:1200px;text-align:center;font-family:"Bebas Neue",Impact,sans-serif;font-weight:400;color:var(--navy);font-size:206px;line-height:206px}
  .ribbon{left:48px;top:458px;width:1116px;height:48px}
  .ribbon-text{left:48px;top:458px;width:1116px;height:48px;line-height:48px;text-align:center;color:#fff;font-family:"Lobster Two",Georgia,cursive;font-style:italic;font-weight:700;font-size:27px;letter-spacing:2px}
  .intro{left:78px;width:1040px;font-weight:600;font-size:19.5px;line-height:29.7px;text-align:justify}
  .section-tag{height:52px;line-height:52px;background:var(--teal);border-radius:26px;padding:0 24px;font-family:"Lobster Two",Georgia,cursive;font-style:italic;font-weight:700;font-size:28px;color:var(--navy);white-space:nowrap}
  .dots-h{border-top:5px dotted var(--navy);height:0}
  .dots-v{border-left:5px dotted var(--navy);width:0}
  .force-art{width:236px;height:236px;border-radius:50%;background:var(--navy);overflow:hidden}
  .force-art span{position:absolute;inset:34px;border-radius:50%}
  .force-label{width:340px;text-align:center;font-family:"Oswald",Arial,sans-serif;font-weight:600;font-size:25px;letter-spacing:1.5px;color:var(--rose)}
  .force-text{width:330px;text-align:center;font-size:19px;line-height:29.7px}
  .placeholder{border-radius:10px}
  .quality-title{font-family:"Oswald",Arial,sans-serif;font-weight:600;font-size:25px;letter-spacing:1px;color:var(--rose)}
  .quality-text{font-size:19px;line-height:29.7px}
  .col-text{font-size:19px;line-height:29.7px}
  .method-badge{left:83px;width:114px;height:114px;border-radius:50%;background:var(--rose)}
  .method-text{left:209px;font-size:19px;line-height:29.7px}
  .questions{left:222px;top:3478px;font-style:italic;font-size:19px;line-height:29.7px;list-style:disc}
  .questions li{margin-bottom:24px}
  .t-list{left:772px;top:3032px;font-size:19px;line-height:41px}
  .t-list b{font-family:"Oswald",Arial,sans-serif;font-weight:500;font-size:24px;letter-spacing:1px}
  .t-list i{font-size:17px}
</style>
</head>
<body>

<h1 class="abs title" style="top:100px;letter-spacing:16px">HIRING THE</h1>
<h1 class="abs title" style="top:278px;letter-spacing:4px">RIGHT PEOPLE</h1>

<svg class="abs ribbon" viewBox="0 0 1116 48" aria-hidden="true">
  <polygon points="0,0 1116,0 1094,24 1116,48 0,48 22,24" fill="var(--red)"/>
</svg>
<p class="abs ribbon-text">Why Potential Trumps Everything Else</p>

<p class="abs intro" style="top:548px">According to global leadership expert Marten Velloso-Quirant, potential tops brains, experience and competencies when evaluating employees. It's the number one predictor of success at all levels in every size organization.</p>
<p class="abs intro" style="top:630px">The hallmarks of potential include the ability to adapt and grow. Because companies operate in an increasingly volatile and complex world, they need employees who can easily acclimate to an ever-changing business environment and grow into challenging new roles. Employees must be able to succeed today and tomorrow, regardless of how much things change.</p>
<p class="abs intro" style="top:754px">That's why you can't use a competency-only based evaluation criteria when hiring. It is just impossible to predict the qualifications needed to succeed down the road. Hiring right means identifying candidates with the greatest potential and helping them flourish once they're on your team.</p>

<!-- Three forces -->
<div class="abs section-tag" style="left:83px;top:946px;width:682px">Three Forces Contributing to Senior Talent Scarcity</div>
<div class="abs dots-h" style="left:775px;top:970px;width:200px"></div>
<div class="abs dots-v" style="left:972px;top:970px;height:55px"></div>

<div class="abs force-art" style="left:96px;top:1038px" role="img" aria-label="Globe illustration showing world continents"><span style="background:var(--globe)"></span></div>
<div class="abs force-art" style="left:488px;top:1038px" role="img" aria-label="Illustration of a group of people representing demographics"><span style="background:var(--red)"></span></div>
<div class="abs force-art" style="left:880px;top:1038px" role="img" aria-label="Illustration of connected pipes representing talent pipelines"><span style="background:var(--orange)"></span></div>

<h2 class="abs force-label" style="left:44px;top:1352px">GLOBALIZATION</h2>
<h2 class="abs force-label" style="left:436px;top:1352px">DEMOGRAPHICS</h2>
<h2 class="abs force-label" style="left:828px;top:1352px">PIPELINES</h2>

<p class="abs force-text" style="left:49px;top:1412px">With the pace of globalization charging full steam ahead, companies in developed and developing nations must compete for talent like never before. For example, the Global Finance Council predicts 70% of the world's growth by 2016 will come from emerging markets.</p>
<p class="abs force-text" style="left:441px;top:1412px">The percentage of senior executives in the sought-after 35-to-44-year-old age group has been dwindling. During the past decade, this demographic shift primarily affected the U.S. and Europe. However, by 2020, Russia, Canada, South Korea and China will have more workers entering retirement than the workforce.</p>
<p class="abs force-text" style="left:833px;top:1412px">Companies remain unsure where they will find the next generation of leaders. According to a Larkspur Advisory 2014 survey of CEOs in 68 countries, 63% of respondents said they were concerned about the future availability of key skills at all levels. In a Harbor Strategy Group study, 56% of executives expect critical gaps in their ability to fill senior managerial roles in coming years.</p>

<div class="abs dots-v" style="left:248px;top:1600px;height:255px"></div>

<!-- Five qualities -->
<div class="abs section-tag" style="left:83px;top:1877px;width:784px">Identifying Employee Potential - The Five Critical Qualities</div>
<div class="abs dots-h" style="left:877px;top:1901px;width:100px"></div>
<div class="abs dots-v" style="left:974px;top:1901px;height:55px"></div>

<div class="abs placeholder" style="left:196px;top:1995px;width:108px;height:44px;background:var(--navy)" role="img" aria-label="Dumbbell icon"></div>
<div class="abs placeholder" style="left:570px;top:1972px;width:86px;height:86px;background:var(--teal)" role="img" aria-label="Magnifying glass icon"></div>
<div class="abs placeholder" style="left:920px;top:1972px;width:52px;height:80px;background:var(--yellow)" role="img" aria-label="Light bulb icon"></div>

<h3 class="abs quality-title" style="left:166px;top:2074px">1. MOTIVATION</h3>
<p class="abs quality-text" style="left:100px;top:2128px;width:340px">A powerful commitment to pursue unselfish goals. Highly ambitious with a strong desire to excel. Seeks big, collective goals and shows profound personal humility.</p>
<h3 class="abs quality-title" style="left:530px;top:2074px">2. CURIOSITY</h3>
<p class="abs quality-text" style="left:511px;top:2128px;width:280px">Pursues new experiences, knowledge and candid feedback. Remains open to learning and change.</p>
<h3 class="abs quality-title" style="left:874px;top:2074px">3. INSIGHT</h3>
<p class="abs quality-text" style="left:846px;top:2128px;width:300px">Gathers and makes sense of information that might lead to new possibilities. Sees connections where others don't.</p>

<div class="abs placeholder" style="left:372px;top:2300px;width:96px;height:100px;background:var(--orange)" role="img" aria-label="Engagement ring icon"></div>
<div class="abs placeholder" style="left:695px;top:2318px;width:140px;height:82px;background:var(--red)" role="img" aria-label="Mountain peak icon"></div>

<h3 class="abs quality-title" style="left:314px;top:2420px">4. ENGAGEMENT</h3>
<p class="abs quality-text" style="left:314px;top:2474px;width:300px">Uses emotion and logic to communicate a persuasive vision. Connects with work and people.</p>
<h3 class="abs quality-title" style="left:653px;top:2420px">5. DETERMINATION</h3>
<p class="abs quality-text" style="left:653px;top:2474px;width:300px">Fights for difficult goals despite challenges and bounces back from adversity.</p>

<svg class="abs" style="left:430px;top:2580px" width="340" height="90" viewBox="0 0 340 90" aria-hidden="true">
  <line x1="118" y1="5" x2="10" y2="82" stroke="var(--navy)" stroke-width="5" stroke-dasharray="4 6"/>
  <line x1="222" y1="5" x2="330" y2="82" stroke="var(--navy)" stroke-width="5" stroke-dasharray="4 6"/>
</svg>

<!-- Evaluate / Retain -->
<div class="abs section-tag" style="left:119px;top:2685px;width:408px">How to Evaluate Potential</div>
<div class="abs section-tag" style="left:630px;top:2685px;width:534px">How to Retain High-Potential Talent</div>
<div class="abs dots-v" style="left:589px;top:2756px;height:820px"></div>

<p class="abs col-text" style="left:166px;top:2800px;width:420px">To determine if a candidate believes in self-improvement, enjoys learning and can recover from missteps, you need to uncover concrete examples by:</p>

<div class="abs method-badge" style="top:2942px" role="img" aria-label="Shovel icon"></div>
<p class="abs method-text" style="top:2970px">Digging into personal<br>and professional histories</p>
<div class="abs method-badge" style="top:3070px" role="img" aria-label="Clipboard icon"></div>
<p class="abs method-text" style="top:3112px">Conducting in-depth interviews</p>
<div class="abs method-badge" style="top:3205px" role="img" aria-label="Magnifying glass icon"></div>
<p class="abs method-text" style="top:3247px">Thoroughly checking references</p>
<div class="abs method-badge" style="top:3348px;background:var(--blush)" role="img" aria-label="Question mark icon"></div>
<p class="abs method-text" style="top:3405px">Asking pointed questions, such as:</p>
<ul class="abs questions">
  <li>How do you react when<br>someone challenges you?</li>
  <li>How do you invite input<br>from others on your team?</li>
</ul>

<p class="abs col-text" style="left:646px;top:2800px;width:310px">Offer development opportunities that push employees out of their comfort zones, but don't stretch them beyond their limits.</p>
<div class="abs placeholder" style="left:980px;top:2785px;width:120px;height:170px;background:linear-gradient(135deg,var(--red),var(--teal))" role="img" aria-label="Hot air balloon illustration"></div>

<p class="abs col-text" style="left:646px;top:2992px">Create autonomy in the four &ldquo;T&rdquo; dimensions:</p>
<div class="abs" style="left:689px;top:3032px;width:76px;height:160px;background:var(--teal-deep)" role="img" aria-label="Large decorative letter T"></div>
<div class="abs t-list">
  <p><b>ASK</b> <i>(what they do)</i></p>
  <p><b>IME</b> <i>(when they do it)</i></p>
  <p><b>EAM</b> <i>(whom they do it with)</i></p>
  <p><b>ECHNIQUE</b> <i>(how they do it)</i></p>
</div>

<div class="abs placeholder" style="left:665px;top:3255px;width:120px;height:118px;background:linear-gradient(90deg,var(--red),var(--teal))" role="img" aria-label="Puzzle pieces illustration"></div>
<p class="abs col-text" style="left:832px;top:3258px;width:320px">Design an environment in which employees can master their skills and excel. Help them by setting difficult, yet attainable, challenges and eliminating distractions.</p>

<p class="abs col-text" style="left:646px;top:3462px;width:330px">Establish a purpose in all work so employees know they're serving something bigger than themselves. Engage them in a greater team</p>
<div class="abs" style="left:988px;top:3425px;width:106px;height:106px;border-radius:50%;background:var(--red)" role="img" aria-label="Flower illustration"></div>

</body>
</html>
```